Business Card Design for Cybersecurity Company - Quorvent Systems

We need a business card design for our new cybersecurity company, Quorvent. We’re going for a clean, hi tech look that feels modern, premium, and trustworthy. We want a design that really stands out and makes people say WOW when we hand it over!

Quorvent delivers reliable IT support and managed services for small and mid sized businesses. We help companies stay secure, efficient, and connected through proactive monitoring, cybersecurity services, cloud management, and remote support.

Target Market(s)

Designers should target small and mid sized businesses that need dependable cybersecurity and IT support.

Industry/Entity Type

Cybersecurity, Managed Service Provider, IT services

Contact Information for Business Card

Contact information

Requirements
Must have
• The card should look clean, modern, and tech focused, with the Quorvent logo, clear contact info, and strong readability. It needs to feel premium and professional while still keeping a simple layout that fits a cybersecurity and IT brand.
Nice to have
• Nice to have elements include subtle touches that give the card a modern, tech feel, along with a layout that works well in different background styles.
Should not have
• The card should avoid clutter, loud graphics, or anything that takes attention away from the logo and contact details.

```html
<!DOCTYPE html>
<html lang="en">
<head>
<meta charset="utf-8">
<title>Quorvent Systems – Business Card</title>
<link href="https://fonts.googleapis.com/css2?family=Montserrat:wght@400;500;600&display=swap" rel="stylesheet">
<style>
  :root {
    --page-bg: #000000;
    --card-white: #ffffff;
    --brand-purple: #6351a8;
    --brand-blue: #4566b0;
    --brand-violet: #7a4ba0;
    --accent-bar: #2b2b30;
    --logo-ink: #5a55ad;
    --text-light: #ffffff;
  }
  * { margin: 0; padding: 0; box-sizing: border-box; }
  html, body {
    width: 805px; height: 1200px; overflow: hidden;
    background: var(--page-bg);
    font-family: "Montserrat", Arial, sans-serif;
  }
  .canvas {
    position: relative; width: 805px; height: 1200px;
  }
  .card {
    position: absolute; left: 122px; width: 560px; height: 320px; overflow: hidden;
  }
  .card-front { top: 230px; background: var(--card-white); }
  .card-back {
    top: 650px;
    background: linear-gradient(90deg, var(--brand-blue) 0%, var(--brand-violet) 100%);
  }
  .front-panel {
    position: absolute; left: 296px; top: 0; width: 264px; height: 320px;
    background: var(--brand-purple);
  }
  .front-bar {
    position: absolute; left: 286px; top: 58px; width: 10px; height: 204px;
    background: var(--accent-bar);
  }
  .brand {
    position: absolute; display: flex; align-items: center; gap: 12px;
  }
  .brand-mark {
    border-radius: 50%; border: 3px solid currentColor; flex: none;
  }
  .brand-text { display: flex; flex-direction: column; font-weight: 500; line-height: 1; }
  .brand-name { letter-spacing: 0.5px; }
  .brand-sub { letter-spacing: 6px; margin-top: 4px; }
  .card-front .brand { left: 28px; top: 122px; color: var(--logo-ink); }
  .card-front .brand-mark { width: 58px; height: 58px; }
  .card-front .brand-name { font-size: 30px; }
  .card-front .brand-sub { font-size: 11px; }
  .card-back .brand { left: 116px; top: 98px; color: var(--text-light); }
  .card-back .brand-mark { width: 86px; height: 86px; }
  .card-back .brand-name { font-size: 40px; }
  .card-back .brand-sub { font-size: 15px; letter-spacing: 8px; }
  .person {
    position: absolute; left: 310px; top: 78px; color: var(--text-light);
  }
  .person-name { font-size: 23px; font-weight: 500; letter-spacing: 0.2px; }
  .person-role { font-size: 6.5px; letter-spacing: 1.2px; margin-top: 3px; padding-left: 6px; }
  .contacts {
    position: absolute; left: 312px; top: 143px; list-style: none; color: var(--text-light);
  }
  .contacts li {
    display: flex; align-items: center; gap: 9px; height: 27px; font-size: 16.5px; font-weight: 400;
  }
  .contacts svg { width: 18px; height: 18px; flex: none; fill: none; stroke: var(--text-light); stroke-width: 1.6; }
</style>
</head>
<body>
<main class="canvas">
  <section class="card card-front" aria-label="Business card front">
    <div class="brand">
      <span class="brand-mark"></span>
      <span class="brand-text"><span class="brand-name">Quorvent</span><span class="brand-sub">Systems</span></span>
    </div>
    <div class="front-panel"></div>
    <div class="front-bar"></div>
    <div class="person">
      <p class="person-name">MARCUS BRENNAN</p>
      <p class="person-role">OWNER | CEO | QUORVENT SYSTEMS</p>
    </div>
    <ul class="contacts">
      <li><svg viewBox="0 0 24 24"><path d="M5 3h4l2 5-2.5 1.5a11 11 0 0 0 6 6L16 13l5 2v4a2 2 0 0 1-2 2A16 16 0 0 1 3 5a2 2 0 0 1 2-2z"/></svg>(855) 402-QRVT</li>
      <li><svg viewBox="0 0 24 24"><rect x="7" y="2" width="10" height="20" rx="2"/><line x1="11" y1="18" x2="13" y2="18"/></svg>(813) 555-0172</li>
      <li><svg viewBox="0 0 24 24"><rect x="3" y="6" width="18" height="12"/><path d="M3 6l9 7 9-7"/></svg>marcus@quorvent.com</li>
      <li><svg viewBox="0 0 24 24"><circle cx="12" cy="12" r="9"/><ellipse cx="12" cy="12" rx="4" ry="9"/><line x1="3" y1="12" x2="21" y2="12"/></svg>www.quorvent.com</li>
    </ul>
  </section>

  <section class="card card-back" aria-label="Business card back">
    <div class="brand">
      <span class="brand-mark"></span>
      <span class="brand-text"><span class="brand-name">Quorvent</span><span class="brand-sub">Systems</span></span>
    </div>
  </section>
</main>
</body>
</html>
```